Velmora Intergrated Marketing Stationary Design Contest

We require a very professional looking stationary set to include: letterhead, compliments slip and business cards (double sided bus cards).

Files should be supplied on either Illustrator or InDesign.

We are interested in perhaps encorporating a faint watermark with the letter q or the logo, but it isnt a pre-requisite

Target Market(s)

Business owners seeking professional marketing services

Industry/Entity Type

Marketing

Requirements
Must have
• Concurrent theme wiht business cards, letterhead and comp slip. Must be an editable document for future ammendment
Should not have
• No use of times new roman or similar fonts

```html
<!DOCTYPE html>
<html lang="en">
<head>
<meta charset="utf-8">
<title>Velmora Intergrated Marketing – Stationery Set</title>
<link rel="stylesheet" href="https://fonts.googleapis.com/css2?family=Montserrat:wght@400;600;700&display=swap">
<style>
  :root {
    --brand-red: #ff1b2b;
    --ink: #111111;
    --paper: #ffffff;
    --edge: #555555;
    --page-bg: #ffffff;
  }
  * { box-sizing: border-box; margin: 0; padding: 0; }
  html, body {
    width: 1200px; height: 793px; overflow: hidden;
    background: var(--page-bg);
    font-family: "Montserrat", Arial, sans-serif;
    color: var(--ink);
  }
  .canvas { position: relative; width: 1200px; height: 793px; }

  .sheet {
    position: absolute;
    background: var(--paper);
    border: 0.6px solid var(--edge);
    overflow: hidden;
  }
  .sheet--red { background: var(--brand-red); border-color: #333; }

  .comp-slip { left: 53px; top: 63px; width: 478px; height: 225px; }
  .comp-slip-back { left: 53px; top: 339px; width: 478px; height: 225px; }
  .card-front { left: 52px; top: 615px; width: 194px; height: 126px; border-width: 1px; border-color: #111; }
  .card-back { left: 337px; top: 615px; width: 194px; height: 126px; }
  .letterhead { left: 669px; top: 63px; width: 478px; height: 676px; }

  .brand {
    position: absolute;
    display: flex; align-items: center;
  }
  .brand-dot {
    border-radius: 50%;
    background: var(--brand-red);
    flex: none;
  }
  .brand-name {
    font-weight: 400;
    color: var(--ink);
    letter-spacing: 0.12em;
    line-height: 1;
  }
  .brand--large { gap: 6px; }
  .brand--large .brand-dot { width: 30px; height: 30px; }
  .brand--large .brand-name { font-size: 24px; }
  .brand--small { gap: 4px; }
  .brand--small .brand-dot { width: 18px; height: 18px; }
  .brand--small .brand-name { font-size: 13px; }

  .block { position: absolute; line-height: 1.2; }
  .address, .contact { font-size: 7.4px; }
  .address .company { font-weight: 700; }
  .address .company--red { color: var(--brand-red); }
  .contact .web { font-weight: 700; }
  .legal { font-size: 4.6px; line-height: 1.25; }

  .card-front .person .name { font-size: 9.4px; font-weight: 700; color: var(--brand-red); line-height: 1; }
  .card-front .person .role { font-size: 6px; font-weight: 700; line-height: 1.3; }
  .card-front .address, .card-front .contact { font-size: 4.9px; line-height: 1.28; }
</style>
</head>
<body>
<main class="canvas">

  <!-- Compliments slip, front -->
  <section class="sheet comp-slip" aria-label="Compliments slip">
    <div class="brand brand--large" style="left:23px; top:25px;">
      <span class="brand-dot"></span><span class="brand-name">Velmora</span>
    </div>
    <address class="block address" style="left:327px; top:21px; font-style:normal;">
      <div class="company company--red">Velmora Intergrated Marketing</div>
      <div>Harbour House</div>
      <div>Linden Row</div>
      <div>Brackley</div>
      <div>North Riding</div>
      <div>BR41 7QN</div>
    </address>
    <div class="block contact" style="left:327px; top:143px;">
      <div class="web">web: www.velmoraim.co.uk</div>
      <div>email: hello@velmoraim.co.uk</div>
      <div>tel: 01632 960418</div>
      <div>fax: 01632 960427</div>
    </div>
    <div class="block legal" style="left:327px; top:187px;">
      <div>Company registration: 5518304</div>
      <div>Vat No: 781 2249 06</div>
      <div>Trading as a division of Brandale Ltd</div>
    </div>
  </section>

  <!-- Compliments slip, reverse -->
  <section class="sheet sheet--red comp-slip-back" aria-label="Compliments slip reverse"></section>

  <!-- Business card, front -->
  <section class="sheet card-front" aria-label="Business card front">
    <div class="brand brand--small" style="left:11px; top:15px;">
      <span class="brand-dot"></span><span class="brand-name">Velmora</span>
    </div>
    <div class="block person" style="left:114px; top:12px;">
      <div class="name">Marcus Hollin</div>
      <div class="role">General Manager</div>
    </div>
    <address class="block address" style="left:114px; top:46px; font-style:normal;">
      <div class="company">Velmora Intergrated Marketing</div>
      <div>Harbour House</div>
      <div>Linden Row</div>
      <div>Brackley</div>
      <div>North Riding</div>
      <div>BR41 7QN</div>
    </address>
    <div class="block contact" style="left:114px; top:90px;">
      <div class="web">www.velmoraim.co.uk</div>
      <div>hello@velmoraim.co.uk</div>
      <div>tel: 01632 960418</div>
      <div>fax: 01632 960427</div>
    </div>
  </section>

  <!-- Business card, reverse -->
  <section class="sheet sheet--red card-back" aria-label="Business card reverse"></section>

  <!-- Letterhead -->
  <section class="sheet letterhead" aria-label="Letterhead">
    <div class="brand brand--large" style="left:34px; top:36px;">
      <span class="brand-dot"></span><span class="brand-name">Velmora</span>
    </div>
    <address class="block address" style="left:336px; top:33px; font-style:normal;">
      <div class="company">Velmora Intergrated Marketing</div>
      <div>Harbour House</div>
      <div>Linden Row</div>
      <div>Brackley</div>
      <div>North Riding</div>
      <div>BR41 7QN</div>
    </address>
    <div class="block contact" style="left:336px; top:580px;">
      <div class="web">web: www.velmoraim.co.uk</div>
      <div>email: hello@velmoraim.co.uk</div>
      <div>tel: 01632 960418</div>
      <div>fax: 01632 960427</div>
    </div>
    <div class="block legal" style="left:336px; top:624px;">
      <div>Company registration: 5518304</div>
      <div>Vat No: 781 2249 06</div>
      <div>Trading as a division of Brandale Ltd</div>
    </div>
  </section>

</main>
</body>
</html>
```